Bright Path Estate Sales web design

We are looking to launch an Estate Sales Website for Nashville, TN. The name of our Business is Bright Path Estate Sales. We would like to give you a blank slate so that you can showcase your design skills for us. The few things we are looking for are a nice header graphic of a house or a stock image of an estate sale. Near the header graphic we would like a quick inquiry form. If not on the right side of the header maybe midway down the site. We potentially want to see what purple and Gold look like on the site however this is not a must. We have over 20 years of industry related experience.

1. Buttons at top of the website will be.
a. Services
b. Upcoming Sales
c. About Us
d. FAQs
e. Resources

Services we offer:
1. Estate Sales
2. Cleanouts
3. Appraisals

Sites We like:
https://www.kelvorintagsales.example/

We don't have a logo yet so if you have ideas please share them with us. Below are 2 ideas however if you have your own thoughts please ignore.

1. Oval ornate frame, gold and black, with BPES in the middle, deep purple. Think of catering to high class people..font should be fancy as opposed to simple.

2. Another option, Bright Path in bold fancy script, same colors, with Estate Sales below, small different font, black.

```html
<!DOCTYPE html>
<html lang="en">
<head>
<meta charset="utf-8">
<title>Bright Path Estate Sales</title>
<link href="https://fonts.googleapis.com/css2?family=Josefin+Sans:wght@300;400;600;700&family=Montserrat:wght@700;800&display=swap" rel="stylesheet">
<style>
:root{
  --purple:#3b0a3d;
  --purple-soft:#4a1450;
  --ink:#1d1d1f;
  --muted:#55525a;
  --paper:#ffffff;
  --mist:#f4f1f2;
  --line:#8a7a8c;
}
*{box-sizing:border-box;margin:0;padding:0}
html,body{width:1200px;height:4511px;overflow:hidden}
body{font-family:"Josefin Sans",sans-serif;color:var(--ink);background:var(--paper);position:relative}
.abs{position:absolute}
.heading{font-family:"Montserrat",sans-serif;font-weight:800;color:var(--purple);text-transform:uppercase;letter-spacing:.5px}
.rule{width:44px;height:3px;background:var(--purple)}
.btn{display:inline-flex;align-items:center;justify-content:center;background:var(--purple);color:#fff;border-radius:24px;font-weight:600;font-size:14px;text-transform:uppercase;letter-spacing:.3px}
.btn.light{background:#fff;color:var(--purple)}

/* hero */
.hero{left:0;top:0;width:1200px;height:695px;background:linear-gradient(180deg,#e6edf5 0%,#d7e1ec 30%,#b7b4b2 55%,#8e8a86 68%,#5f6d3c 82%,#3d4e2a 100%)}
.brand{left:137px;top:22px;color:var(--purple);font-weight:600;line-height:1}
.brand .name{font-size:40px;display:block}
.brand .sub{font-size:21px;display:block;margin-top:6px;padding-left:44px}
.nav{left:476px;top:46px;display:flex;gap:42px;font-size:15px;font-weight:600;text-transform:uppercase;color:var(--ink)}
.hero-title{left:0;top:122px;width:1200px;text-align:center;font-family:"Montserrat",sans-serif;font-weight:800;font-size:33px;line-height:48px;color:var(--purple)}
.hero .btn{left:475px;top:236px;width:250px;height:45px;font-size:13px}

/* upcoming sales */
.sales-head{left:0;top:736px;width:1200px;text-align:center;font-size:30px}
.sales-rule{left:578px;top:802px}
.arrow{top:738px}
.sale-card{top:851px;width:273px;height:388px;background:#fff;box-shadow:0 4px 18px rgba(0,0,0,.09)}
.sale-card .photo{height:210px}
.sale-card h3{margin:30px 0 0 29px;font-family:"Montserrat",sans-serif;font-weight:700;font-size:15px;color:var(--purple);text-decoration:underline;text-underline-offset:3px}
.sale-card p{margin:20px 0 0 29px;font-size:13px;line-height:21px;color:var(--ink)}
.sale-card .date{margin-top:20px;margin-left:33px}
.view-all{left:522px;top:1277px;width:156px;height:46px}

/* about */
.about-photo{left:0;top:1375px;width:568px;height:514px;background:linear-gradient(180deg,#c9c6bf 0%,#a9aeaa 45%,#6f8a43 72%,#5b7a2f 100%)}
.about-text{left:568px;top:1375px;width:632px;height:514px;background:var(--mist)}
.about-text h2{position:absolute;left:52px;top:62px;font-size:28px}
.about-text .rule{position:absolute;left:52px;top:114px}
.about-text p{position:absolute;left:52px;top:150px;width:462px;font-size:15px;line-height:25.6px;color:var(--muted)}
.about-text .btn{position:absolute;left:54px;top:404px;width:137px;height:46px}

/* services */
.services-head{left:0;top:1942px;width:1200px;text-align:center;font-size:29px}
.services-rule{left:578px;top:2002px}
.service{top:2046px;width:295px;height:417px;background:var(--purple);border-radius:10px;color:#fff;text-align:center}
.service svg{margin-top:40px}
.service h3{margin-top:14px;font-family:"Montserrat",sans-serif;font-weight:800;font-size:18px;text-transform:uppercase}
.service p{margin:22px auto 0;width:214px;font-size:14px;line-height:21px;color:#e8dcea}
.service .btn{margin-top:26px;width:136px;height:44px}

/* resources */
.resources{left:0;top:2527px;width:1200px;height:653px;background:linear-gradient(180deg,#4b6f93 0%,#7b93ad 40%,#9a8e8a 70%,#5b4a45 100%)}
.resources-head{left:0;top:2570px;width:1200px;text-align:center;font-size:29px;color:#fff}
.resources-rule{left:578px;top:2630px;background:#fff}
.res-card{top:2675px;width:294px;height:461px;background:#fff;border-radius:10px;overflow:hidden}
.res-card .photo{height:180px}
.res-card h3{margin:30px 28px 0;font-family:"Montserrat",sans-serif;font-weight:700;font-size:13.5px;line-height:21px;text-transform:uppercase}
.res-card p{margin:14px 28px 0;font-size:13.5px;line-height:21px;color:var(--muted)}
.res-card .btn{position:absolute;left:29px;top:390px;width:136px;height:44px}

/* quote */
.quote{left:0;top:3180px;width:1200px;height:625px;background:var(--mist)}
.quote-head{left:0;top:3230px;width:1200px;text-align:center;font-size:29px}
.quote-rule{left:578px;top:3290px}
.quote-frame{left:210px;top:3337px;width:778px;height:468px;background:var(--purple);border-radius:48px 48px 0 0}
.quote-form{left:230px;top:3357px;width:738px;height:448px;background:#fff;border-radius:34px 34px 0 0}
.field{position:absolute;border:1.5px solid var(--line);border-radius:18px;font-size:14px;color:var(--muted);padding:0 20px;display:flex;align-items:center}
.field.area{align-items:flex-start;padding-top:18px;border-radius:20px}
.quote-form .btn{position:absolute;left:306px;top:370px;width:127px;height:44px;font-size:18px;border-radius:22px}

/* faq */
.faq{left:0;top:3805px;width:1200px;height:373px;background:var(--purple);color:#fff}
.faq h2{position:absolute;left:140px;top:98px;font-family:"Montserrat",sans-serif;font-weight:800;font-size:28px}
.faq .rule{position:absolute;left:140px;top:143px;background:#fff;width:64px}
.faq .btn{position:absolute;left:138px;top:191px;width:162px;height:43px;font-size:13px;font-weight:700}
.faq ul{position:absolute;left:484px;top:10px;width:585px;list-style:none}
.faq li{height:58px;border-bottom:1.5px solid rgba(255,255,255,.55);display:flex;align-items:center;justify-content:space-between;padding:0 28px;font-size:18px;font-weight:300}
.faq li span.plus{font-size:18px}

/* footer */
.foot-brand{left:175px;top:4255px;color:var(--purple);font-weight:600;line-height:1}
.foot-brand .name{font-size:46px;display:block}
.foot-brand .sub{font-size:22px;display:block;margin-top:8px;padding-left:46px}
.foot-col{top:4210px;font-size:11.5px;line-height:15px}
.foot-col h4{font-weight:700;font-size:13px;text-transform:uppercase;margin-bottom:18px}
.contact-row{display:flex;gap:14px;margin-bottom:18px;align-items:flex-start}
.contact-row svg{margin-top:6px;flex:none}
.menu-list{list-style:none}
.menu-list li{margin-bottom:4px}
.social-row{display:flex;gap:18px;align-items:center;margin-bottom:20px}
.social-dot{width:10px;height:10px;border-radius:50%;background:var(--ink);flex:none}
.foot-line{left:135px;top:4427px;width:934px;height:2px;background:var(--purple)}
.copyright{left:0;top:4462px;width:1200px;text-align:center;font-size:10.5px;color:var(--muted)}
</style>
</head>
<body>

<!-- hero -->
<section class="abs hero" role="img" aria-label="Photo of a large grey shingled house with a white wraparound porch, trees and a green lawn"></section>
<div class="abs brand"><span class="name">Bright Path</span><span class="sub">Estate Sales</span></div>
<nav class="abs nav"><span>Services</span><span>Upcoming Sales</span><span>About Us</span><span>FAQs</span><span>Resources</span></nav>
<h1 class="abs hero-title">WE HAVE OVER 20 YEARS OF<br>INDUSTRY RELATED EXPERIENCE</h1>
<a class="abs btn" style="left:475px;top:236px;width:250px;height:45px;font-size:13px">Schedule a consultation</a>

<!-- upcoming sales -->
<h2 class="abs heading sales-head">Upcoming Sales</h2>
<div class="abs rule sales-rule"></div>
<svg class="abs arrow" style="left:373px" width="32" height="56" viewBox="0 0 32 56"><path d="M28 2 L4 28 L28 54" fill="none" stroke="#3b0a3d" stroke-width="3"/></svg>
<svg class="abs arrow" style="left:796px" width="32" height="56" viewBox="0 0 32 56"><path d="M4 2 L28 28 L4 54" fill="none" stroke="#3b0a3d" stroke-width="3"/></svg>

<article class="abs sale-card" style="left:32px">
  <div class="photo" role="img" aria-label="Photo of a white modern house with a pool and palm trees" style="background:linear-gradient(180deg,#9fc3e6,#e9ecef 55%,#5fb8d2)"></div>
  <h3>NASHVILLE ESTATE</h3><p>123 Main Street, Nashville,<br>TN 37201</p><p class="date">February 9-11</p>
</article>
<article class="abs sale-card" style="left:322px">
  <div class="photo" role="img" aria-label="Photo of a grey stone-faced house among palm trees" style="background:linear-gradient(180deg,#8fb2d6,#a9a7a2 50%,#5d7d3e)"></div>
  <h3>NASHVILLE ESTATE</h3><p>123 Main Street, Nashville,<br>TN 37201</p><p class="date">February 9-11</p>
</article>
<article class="abs sale-card" style="left:613px">
  <div class="photo" role="img" aria-label="Photo of a brick manor house behind a hedge and pond" style="background:linear-gradient(180deg,#7b9a5c,#8e7f66 50%,#3f5a32)"></div>
  <h3>NASHVILLE ESTATE</h3><p>123 Main Street, Nashville,<br>TN 37201</p><p class="date">February 9-11</p>
</article>
<article class="abs sale-card" style="left:902px">
  <div class="photo" role="img" aria-label="Photo of a blue-grey house behind a white picket fence" style="background:linear-gradient(180deg,#c9dcef,#8ea0b4 55%,#e4e4e2)"></div>
  <h3>NASHVILLE ESTATE</h3><p>123 Main Street, Nashville,<br>TN 37201</p><p class="date">February 9-11</p>
</article>
<a class="abs btn view-all">View all sales</a>

<!-- about -->
<div class="abs about-photo" role="img" aria-label="Photo of a family walking across a lawn toward a grey house"></div>
<section class="abs about-text">
  <h2 class="heading">About Us</h2>
  <div class="rule"></div>
  <p>Sed ut perspiciatis unde omnis iste natus error sit voluptatem accusantium doloremque laudantium, totam rem aperiam, eaque ipsa quae ab illo inventore veritatis et quasi architecto beatae vitae dicta sunt explicabo. Nemo enim ipsam voluptatem quia voluptas sit aspernatur aut odit aut fugit, sed quia consequuntur magni dolores eos qui ratione voluptatem sequi nesciunt. Neque porro quisquam est, qui dolorem ipsum quia dolor sit amet, consectetur, adipisci velit, sed quia non numquam eius modi tempora incidunt.</p>
  <a class="btn">Read more</a>
</section>

<!-- services -->
<h2 class="abs heading services-head">Our Services</h2>
<div class="abs rule services-rule"></div>

<article class="abs service" style="left:131px">
  <svg width="64" height="64" viewBox="0 0 64 64" fill="none" stroke="#fff" stroke-width="2"><path d="M6 30 L32 8 L58 30"/><path d="M12 26 V58 H52 V26"/><rect x="22" y="32" width="20" height="20"/><path d="M32 32 V52 M22 42 H42"/><path d="M44 14 V20"/></svg>
  <h3>Estate Sales</h3>
  <p>At vero eos et accusamus et iusto odio dignissimos ducimus qui blanditiis praesentium voluptatum deleniti atque corrupti quos dolores et quas molestias excepturi</p>
  <a class="btn light">Read more</a>
</article>
<article class="abs service" style="left:452px">
  <svg width="64" height="64" viewBox="0 0 64 64" fill="none" stroke="#fff" stroke-width="2"><circle cx="32" cy="32" r="28"/><path d="M16 32 L32 18 L48 32"/><path d="M20 30 V46 H44 V30"/><rect x="28" y="36" width="8" height="10" fill="#fff"/></svg>
  <h3>Cleanouts</h3>
  <p>At vero eos et accusamus et iusto odio dignissimos ducimus qui blanditiis praesentium voluptatum deleniti atque corrupti quos dolores et quas molestias excepturi</p>
  <a class="btn light">Read more</a>
</article>
<article class="abs service" style="left:774px">
  <svg width="64" height="64" viewBox="0 0 64 64" fill="none" stroke="#fff" stroke-width="2"><rect x="12" y="8" width="32" height="48" rx="3"/><rect x="18" y="16" width="6" height="6"/><rect x="18" y="28" width="6" height="6"/><rect x="18" y="40" width="6" height="6"/><path d="M28 19 H38 M28 31 H38 M28 43 H36"/><path d="M54 14 L40 44 L38 52 L44 46 L58 16 Z"/></svg>
  <h3>Appraisals</h3>
  <p>At vero eos et accusamus et iusto odio dignissimos ducimus qui blanditiis praesentium voluptatum deleniti atque corrupti quos dolores et quas molestias excepturi</p>
  <a class="btn light">Read more</a>
</article>

<!-- resources -->
<section class="abs resources" role="img" aria-label="Photo of a city skyline at dusk"></section>
<h2 class="abs heading resources-head">Resources</h2>
<div class="abs rule resources-rule"></div>

<article class="abs res-card" style="left:130px">
  <div class="photo" role="img" aria-label="Photo of hands at a laptop beside a rising chart" style="background:linear-gradient(135deg,#1c1c1e,#6d6d70 60%,#e2e2e2)"></div>
  <h3>At vero eos et accus<br>amus et iusto odio</h3>
  <p>At vero eos et accusamus et iusto odio dignissimos ducimus qui blan ditiis praesentium voluptatum deleniti atque corrupti quos dolores et quas molestias excepturi</p>
  <a class="btn">Read more</a>
</article>
<article class="abs res-card" style="left:452px">
  <div class="photo" role="img" aria-label="Photo of a riverside city skyline at sunset" style="background:linear-gradient(180deg,#4a3f8f,#c85a9a 50%,#2a1f4a)"></div>
  <h3>At vero eos et accus<br>amus et iusto odio</h3>
  <p>At vero eos et accusamus et iusto odio dignissimos ducimus qui blan ditiis praesentium voluptatum deleniti atque corrupti quos dolores et quas molestias excepturi</p>
  <a class="btn">Read more</a>
</article>
<article class="abs res-card" style="left:773px">
  <div class="photo" role="img" aria-label="Photo of a lit house with a stone path at dusk" style="background:linear-gradient(180deg,#6f8db0,#4a5a66 55%,#4b6a33)"></div>
  <h3>At vero eos et accus<br>amus et iusto odio</h3>
  <p>At vero eos et accusamus et iusto odio dignissimos ducimus qui blan ditiis praesentium voluptatum deleniti atque corrupti quos dolores et quas molestias excepturi</p>
  <a class="btn">Read more</a>
</article>

<!-- quote -->
<section class="abs quote"></section>
<h2 class="abs heading quote-head">Get a Quote</h2>
<div class="abs rule quote-rule"></div>
<div class="abs quote-frame"></div>
<form class="abs quote-form">
  <div class="field" style="left:42px;top:44px;width:316px;height:52px">First Name</div>
  <div class="field" style="left:378px;top:44px;width:316px;height:52px">Last Name</div>
  <div class="field" style="left:42px;top:118px;width:316px;height:52px">Email id</div>
  <div class="field" style="left:378px;top:118px;width:316px;height:52px">Phone</div>
  <div class="field area" style="left:42px;top:188px;width:652px;height:150px">Message</div>
  <a class="btn">Submit</a>
</form>

<!-- faq -->
<section class="abs faq">
  <h2>FAQ</h2>
  <div class="rule"></div>
  <a class="btn light">View all FAQs</a>
  <ul>
    <li><span>At vero eos et accus amus et iusto odio?</span><span class="plus">+</span></li>
    <li><span>On the other hand, we denounce with right?</span><span class="plus">+</span></li>
    <li><span>When our power of choice is untrammelled?</span><span class="plus">+</span></li>
    <li><span>Nam libero tempore, cum soluta nobis est eligendi?</span><span class="plus">+</span></li>
    <li style="border-bottom:none"><span>Temporibus autem quibusdam et aut officiis deb?</span><span class="plus">+</span></li>
  </ul>
</section>

<!-- footer -->
<div class="abs foot-brand"><span class="name">Bright Path</span><span class="sub">Estate Sales</span></div>

<div class="abs foot-col" style="left:452px">
  <h4>Contact Us</h4>
  <div class="contact-row"><svg width="8" height="11" viewBox="0 0 8 11"><path d="M4 0 A4 4 0 0 1 8 4 C8 7 4 11 4 11 C4 11 0 7 0 4 A4 4 0 0 1 4 0Z" fill="#1d1d1f"/><circle cx="4" cy="4" r="1.5" fill="#fff"/></svg><span>418 Larkfield Row,<br>Nashville, TN 37209</span></div>
  <div class="contact-row"><svg width="10" height="10" viewBox="0 0 10 10"><path d="M2 0 L4 2.5 L3 4 C4 6 5 7 6 7 L7.5 6 L10 8 L8.5 10 C4 10 0 6 0 1.5Z" fill="#1d1d1f"/></svg><span>Call Us<br>+1 615 555 0147</span></div>
  <div class="contact-row"><svg width="11" height="8" viewBox="0 0 11 8"><rect width="11" height="8" fill="#1d1d1f"/><path d="M0 0 L5.5 4.5 L11 0" stroke="#fff" fill="none"/></svg><span>E mail Us<br>hello@brightpathsales.example</span></div>
</div>

<div class="abs foot-col" style="left:750px">
  <h4>Menu</h4>
  <ul class="menu-list"><li>Services</li><li>Upcoming Sales</li><li>About Us</li><li>FAQs</li><li>Resources</li></ul>
</div>

<div class="abs foot-col" style="left:964px">
  <h4>Follow Us</h4>
  <div class="social-row"><span class="social-dot"></span><span>Like us on<br>FRONTPORCH</span></div>
  <div class="social-row"><span class="social-dot"></span><span>Follow us on<br>LINKWORK</span></div>
  <div class="social-row"><span class="social-dot"></span><span>Follow us on<br>SNAPGRID</span></div>
</div>

<div class="abs foot-line"></div>
<p class="abs copyright">Copyright © 2024 All Rights Reserved</p>

</body>
</html>
```